**** Web design project for BoltNet ****

For my ICT company BoltNet I need a website.

We design, build and host web-applications and we have our own CMS product. In the references part we want to show sample websites (thumbnails) + links.

It should look modern (WEB 2.0), rounded corners.

I want the following menu' s:
- Home
- Services
- References
- News
- About BoltNet
- Contact

Sample websites:
See attachments
http://www.vandoqa.com
http://www.greyfoxmanagement.nl

Reason: Want to take some time for feedback and improvements.

Reason: I'm waiting for a black background, with shadow and ambient light. You'll make a good chance!

Industry/Entity Type

It Company

Requirements
Must have
• - Fixed width (1024px), should fit on an IPad2
- Language selection English/Dutch
- Twitter/Facebook/LinkedIn/RSS icons
- Footer for Terms of use and Copyrights
- Search box
- 3 (or more) boxes for information i.e. news, blog or advertisements
Nice to have
• - Footer Site Map
- Contrasting background outside borders
- wide image (rotator) (with transperant sentence block)
- Shadow

```html
<!DOCTYPE html>
<html lang="en">
<head>
<meta charset="utf-8">
<title>BoltNet</title>
<link href="https://fonts.googleapis.com/css2?family=Arimo:wght@400;700&display=swap" rel="stylesheet">
<style>
:root{
  --ink:#2f3d4a;
  --text:#555d63;
  --navy:#1d3e5c;
  --teal:#1f8fb8;
  --teal-dark:#0f6a8e;
  --cyan:#10b4dc;
  --green:#55c40a;
  --blue-box:#24507d;
  --line:#d9dde0;
  --link:#3b4b58;
  --social-1:#1e6fb3;
  --social-2:#1fa6d2;
  --social-3:#1a5f9e;
  --social-4:#ec5a3a;
}
*{margin:0;padding:0;box-sizing:border-box}
html,body{width:1156px;height:1200px;overflow:hidden}
body{font-family:"Arimo",Helvetica,Arial,sans-serif;color:var(--text);background:linear-gradient(#e6e8ea 0,#f7f8f8 160px,#fff 600px);position:relative}
.abs{position:absolute}
.lang{left:878px;top:0;width:132px;height:27px;background:#fff;border:1px solid #dadcde;border-top:0;border-radius:0 0 4px 4px;font-size:12px;color:#444;display:flex;align-items:center}
.lang span{padding:0 12px 0 15px;border-right:1px solid #dadcde;line-height:27px}
.lang svg{margin-left:8px}
.brand{left:158px;top:44px;display:flex;align-items:center;gap:10px;font-size:30px;color:var(--teal);letter-spacing:1px}
.brand i{width:22px;height:22px;border-radius:50%;background:var(--teal);display:block}
.phone{left:703px;top:61px;width:305px;height:33px;background:#fff;border-radius:4px;box-shadow:0 1px 4px rgba(0,0,0,.2);display:flex;align-items:center;font-size:13.5px;color:var(--navy)}
.phone .ic{width:58px;height:33px;background:var(--teal);clip-path:polygon(0 0,80% 0,100% 50%,80% 100%,0 100%);border-radius:4px 0 0 4px;display:flex;align-items:center;padding-left:10px;margin-right:8px}
.nav{left:145px;top:110px;width:866px;height:34px;border-radius:4px;background:linear-gradient(#2aa3cb,#137aa3 55%,#0e6d93);box-shadow:0 4px 6px -3px rgba(0,0,0,.35);display:flex}
.nav a{color:#fff;text-decoration:none;font-size:14px;padding:0 14px;line-height:34px;border-right:1px solid rgba(255,255,255,.2)}
.nav a.on{font-weight:700;background:rgba(255,255,255,.08)}
.search{left:777px;top:116px;width:199px;height:21px;background:#fff;border-radius:3px;font-size:12px;color:#999;text-align:right;padding-right:8px;line-height:21px}
.nav-search-ic{left:981px;top:117px}
.banner{left:147px;top:162px;width:861px;height:277px;border-radius:3px;overflow:hidden;box-shadow:0 5px 8px -3px rgba(0,0,0,.4);background:radial-gradient(circle at 88% 45%,#b9e6fb 0,#4aa8dd 12%,#1e5e9c 35%,#1a4a82 60%,#1b3f6e 100%)}
.banner h1{position:absolute;left:67px;top:123px;font-size:38px;color:#fff;font-weight:400}
.banner h1 b{font-weight:700}
.banner p{position:absolute;left:71px;top:170px;font-size:19px;color:#fff}
.arrow{top:274px;width:34px;height:43px;background:linear-gradient(#3a8fbf,#1d5e8c);display:flex;align-items:center;justify-content:center}
.feature{top:452px;width:278px;height:107px;border-radius:3px;color:#fff;display:flex}
.feature .pic{width:72px;height:72px;margin:18px 16px 0 14px;border-radius:50%;background:rgba(255,255,255,.25)}
.feature h2{font-size:23px;font-weight:400;margin-top:11px}
.feature p{font-size:11px;line-height:14.5px;margin-top:6px;width:165px}
.f-com{left:147px;background:linear-gradient(#1ec8ef,var(--cyan) 60%,#0ea0c8)}
.f-tec{left:438px;background:linear-gradient(#6ad812,var(--green) 60%,#45a808)}
.f-svc{left:728px;background:linear-gradient(#2e6195,var(--blue-box) 60%,#1b3e63)}
.panel{top:572px;height:239px;background:#fff;border:1px solid var(--line);border-radius:3px}
.panel h3{font-size:18px;font-weight:400;color:var(--navy);display:flex;align-items:center;gap:10px;margin:14px 0 0 18px}
.panel h3 i{width:20px;height:20px;border-radius:50%;background:var(--teal);display:block}
.about{left:147px;width:563px}
.about p{font-size:11.2px;line-height:17.2px;margin:14px 36px 0 26px;color:var(--text)}
.about p+p{margin-top:17px}
.news{left:724px;width:281px}
.news h3 i{border-radius:2px;background:linear-gradient(#eef5e8,#d7e6cf);border:1px solid #9bbf88;width:25px;height:22px}
.news ul{list-style:none;margin:12px 16px 0 14px}
.news li{border-bottom:1px solid var(--line);padding-bottom:6px;margin-bottom:10px}
.news li:last-child{border:0}
.news b{display:block;font-weight:400;font-size:12.4px;color:var(--navy)}
.news span{display:block;font-size:11px;line-height:14px;margin-top:5px}
.partners{left:152px;top:827px;width:852px;height:56px;display:flex;justify-content:space-between;align-items:center}
.partners div{background:#dcdedf;border-radius:4px}
.foot{left:147px;top:896px;width:858px;height:240px;background:#fff;border:1px solid var(--line);border-radius:3px;display:flex}
.col{border-right:1px solid var(--line);padding:18px 0 0 30px}
.col h4{font-size:15.5px;font-weight:400;color:var(--navy);margin-bottom:14px;letter-spacing:.2px}
.col a{display:block;font-size:10.3px;color:var(--link);text-decoration:none;line-height:19.7px;padding-left:1px}
.contact{padding:24px 0 0 27px;border:0}
.contact .fbrand{display:flex;align-items:center;gap:10px;font-size:28px;color:#c4c8cb;letter-spacing:1px;margin-bottom:20px}
.contact .fbrand i{width:54px;height:54px;border-radius:50%;background:#e6e8e9;display:block}
.contact p{font-size:10.6px;color:var(--ink);line-height:19.8px}
.social{display:flex;gap:8px;margin-top:21px}
.social span{width:41px;height:39px;border-radius:2px;display:block}
.social .s1{background:var(--social-1)}
.social .s2{background:var(--social-2)}
.social .s3{background:var(--social-3)}
.social .s4{background:var(--social-4)}
.bottom{left:0;top:1160px;width:1156px;text-align:center;font-size:10.5px;color:var(--ink)}
.bottom a{color:var(--ink);text-decoration:none}
.bottom em{font-style:normal;margin:0 8px}
</style>
</head>
<body>

<div class="abs lang"><span>Language</span>
  <svg width="24" height="14" viewBox="0 0 24 14"><rect width="24" height="14" fill="#1f3f8c"/><path d="M0 0L24 14M24 0L0 14" stroke="#fff" stroke-width="3"/><path d="M10 0h4v14h-4zM0 5h24v4H0z" fill="#fff"/><path d="M11 0h2v14h-2zM0 6h24v2H0z" fill="#d22"/></svg>
  <svg width="10" height="8" viewBox="0 0 10 8" style="margin-left:5px"><path d="M1 1h8L5 7z" fill="#666"/></svg>
</div>

<div class="abs brand"><i></i>BoltNet</div>

<div class="abs phone"><span class="ic">
  <svg width="22" height="22" viewBox="0 0 22 22"><circle cx="11" cy="11" r="10" fill="none" stroke="#fff" stroke-width="1.6"/><path d="M8 6c1 0 1.5 2 1.3 2.6L8.5 9.4c.6 1.6 2.2 3.2 3.9 3.9l.8-.8c.6-.2 2.6.3 2.6 1.3 0 1-1.2 2-2.2 1.8C10.3 15 7 11.7 6.3 8.4 6 7.2 7 6 8 6z" fill="#fff"/></svg>
</span>+41 - 0522 3184470,&nbsp; +0971 5520396</div>

<nav class="abs nav">
  <a href="#" style="padding:0 16px 0 17px">Home</a>
  <a href="#" class="on">Services</a>
  <a href="#" style="padding:0 14px 0 20px">References</a>
  <a href="#">News</a>
  <a href="#">About BoltNet</a>
  <a href="#" style="border:0">Contact</a>
</nav>
<div class="abs search">search</div>
<svg class="abs nav-search-ic" width="20" height="20" viewBox="0 0 20 20"><circle cx="8" cy="8" r="6" fill="none" stroke="#fff" stroke-width="2"/><path d="M12.5 12.5L18 18" stroke="#fff" stroke-width="2.4" stroke-linecap="round"/></svg>

<section class="abs banner" role="img" aria-label="Glowing digital globe made of binary numbers on a deep blue background">
  <h1><b>System</b> integration</h1>
  <p>Wearing solutions for enhanced custamer experiances</p>
</section>
<div class="abs arrow" style="left:139px"><svg width="14" height="20" viewBox="0 0 14 20"><path d="M11 2L3 10l8 8" fill="none" stroke="#fff" stroke-width="3"/></svg></div>
<div class="abs arrow" style="left:982px"><svg width="14" height="20" viewBox="0 0 14 20"><path d="M3 2l8 8-8 8" fill="none" stroke="#fff" stroke-width="3"/></svg></div>

<div class="abs feature f-com"><div class="pic" role="img" aria-label="Globe with tools icon"></div><div><h2>Communication</h2><p>It was popularised in the 1960s with the release of Lettrafix sheets containing Lorem Ipsum</p></div></div>
<div class="abs feature f-tec"><div class="pic" role="img" aria-label="Desktop computer with gears icon"></div><div><h2>Technology</h2><p>It was popularised in the 1960s with the release of Lettrafix sheets containing Lorem Ipsum</p></div></div>
<div class="abs feature f-svc"><div class="pic" role="img" aria-label="Business team figures icon"></div><div><h2>Services</h2><p>It was popularised in the 1960s with the release of Lettrafix sheets containing Lorem Ipsum</p></div></div>

<section class="abs panel about">
  <h3><i></i>About the company</h3>
  <p>Lorem Ipsum is simply dummy text of the printing and typesetting industry. Lorem Ipsum has been the industry's standard dummy text ever since the 1500s, when an unknown printer took a galley of type and scrambled it to make a type specimen book. It has survived not only five centuries, but also the leap into electronic typesetting, remaining essentially unchanged. It was popularised in the 1960s with the release of Lettrafix sheets containing Lorem Ipsum passages, and more recently with desktop publishing software like Pagecraft Studio including versions of Lorem Ipsum.</p>
  <p>&nbsp;It was popularised in the 1960s with the release of Lettrafix sheets containing Lorem Ipsum passages, and more recently with desktop publishing software like Pagecraft Studio including versions of Lorem Ipsum.</p>
</section>

<section class="abs panel news">
  <h3><i></i>Latest News</h3>
  <ul>
    <li><b>Lorem Ipsum is simply dummy text</b><span>Lorem Ipsum is simply dummy text of the printing and typesetting industry.</span></li>
    <li><b>Lorem Ipsum is simply dummy text</b><span>Lorem Ipsum is simply dummy text of the printing and typesetting industry.</span></li>
    <li><b>Lorem Ipsum is simply dummy text</b><span>Lorem Ipsum is simply dummy text of the printing and typesetting industry.</span></li>
  </ul>
</section>

<div class="abs partners" aria-label="Partner badges">
  <div style="width:120px;height:44px"></div>
  <div style="width:155px;height:38px"></div>
  <div style="width:122px;height:50px"></div>
  <div style="width:94px;height:50px"></div>
  <div style="width:108px;height:42px"></div>
  <div style="width:76px;height:32px"></div>
</div>

<footer class="abs foot">
  <div class="col" style="width:165px">
    <h4>PRODUCTS</h4>
    <a href="#">WebForm AJAX Controls</a><a href="#">Web MVC Extensions</a><a href="#">Rich Client Controls</a><a href="#">Desktop UI Controls</a><a href="#">Forms Controls</a><a href="#">Mobile Toolkit</a><a href="#">Vandoqa Reporting</a><a href="#">Vandoqa DataBridge ORM</a><a href="#">CodePilot</a>
  </div>
  <div class="col" style="width:150px;padding-left:20px">
    <h4>SERVICES</h4>
    <a href="#">Business-User Training</a><a href="#">Developer Training</a><a href="#">Administrator Training</a><a href="#">Designer Training</a><a href="#">Consulting</a><a href="#">Support</a><a href="#">Design &amp; Development</a><a href="#">Developer Training</a><a href="#">Administrator Training</a>
  </div>
  <div class="col" style="width:131px;padding-left:12px">
    <h4>COMMUNITY</h4>
    <a href="#">Support Center</a><a href="#">Announcements</a><a href="#">Documentation</a><a href="#">Forums</a><a href="#">Webinars</a><a href="#">Videos</a><a href="#">Code Library</a><a href="#">Issue Tracker</a><a href="#">Knowledge Base</a>
  </div>
  <div class="col" style="width:172px;padding-left:24px">
    <h4>ABOUT US</h4>
    <a href="#">About Us</a><a href="#">The Vandoqa Difference</a><a href="#">Customers &amp; Testimonials</a><a href="#">Awards</a><a href="#">Press Center</a><a href="#">Events</a><a href="#">Follow Us</a><a href="#">Career Opportunities</a><a href="#">Management</a>
  </div>
  <div class="col contact">
    <div class="fbrand"><i></i>BoltNet</div>
    <p>Tel. Sales &amp; Advies: +31 (0)655 - 18 40 72</p>
    <p>Tel. Algemeen: +31 (0)618 - 27 35 64</p>
    <p>Fax +31 (0)477 - 63 12 05</p>
    <div class="social">
      <span class="s1" role="img" aria-label="Social profile link"></span>
      <span class="s2" role="img" aria-label="Social profile link"></span>
      <span class="s3" role="img" aria-label="Social profile link"></span>
      <span class="s4" role="img" aria-label="News feed link"></span>
    </div>
  </div>
</footer>

<div class="abs bottom">
  <a href="#">Contact Us</a><em>|</em><a href="#">Site Feedback</a><em>|</em><a href="#">Terms of Use</a><em>|</em><a href="#">Privacy Policy</a><em>|</em>Copyright © 2002-2012 BoltNet . All rights reserved.
</div>

</body>
</html>
```